Webpage for a treatment housing for young addicts.

I need a new design and files for my wordpress page. I need it to be more neat and clean. I need it to look professional with a starting page that will work as a navigation. I need like logo and phone number and such up top, a picture under it with one sentence as a slogan and under it 6 boxes to click to come to our different pages. Under it I want news etc.

Target Market(s)

Social services, employees and governements

Coding

Coded - Design and coding required

Font styles to use
Sans Serif

Colors
abd037
3176b5
9d9d9d
aaaaaa
f04a50

Requirements
Must have
• A nice design
Nice to have
• need it to look professional with a starting page that will work as a navigation. I need like logo and phone number and such up top, a picture under it with one sentence as a slogan and under it 6 boxes to click to come to our different pages. Under it I want news etc.
• today www.kelmora.se
• want more like www.trivest.se or www.solbrink.se
Should not have
• To many different colours and a messy design.

```html
<!DOCTYPE html>
<html lang="sv">
<head>
<meta charset="utf-8">
<title>Kelmora – Omsorg Vård Boende</title>
<link href="https://fonts.googleapis.com/css2?family=Jost:wght@400;500;600&family=Lato:wght@400;700&display=swap" rel="stylesheet">
<style>
:root{
  --green:#abd037;
  --blue:#3176b5;
  --navy:#1a4f9c;
  --ink:#333;
  --muted:#777;
  --line:#e2e2e2;
  --soft:#f2f2f2;
  --bar:#3a3a3a;
  --brand:linear-gradient(135deg,var(--navy) 0%,var(--blue) 45%,var(--green) 100%);
}
*{box-sizing:border-box;margin:0;padding:0}
html,body{width:688px;height:1200px;overflow:hidden}
body{position:relative;font-family:"Lato",sans-serif;color:var(--ink);background:#fff;font-size:7px}
.abs{position:absolute}
h2{font-family:"Jost",sans-serif;font-weight:400;font-size:15px;color:#444;text-align:center}
.rule{width:22px;height:1.5px;background:var(--brand);margin:7px auto 0}

/* top bar */
.topbar{left:0;top:0;width:688px;height:12px;background:var(--bar);color:#ddd;font-size:5px;display:flex;align-items:center;justify-content:flex-end;padding-right:134px;gap:6px}
.topbar .dot{width:6px;height:6px;border-radius:50%;background:#888}

/* header */
.header{left:0;top:12px;width:688px;height:42px;background:#fff}
.logo{left:134px;top:10px;display:flex;align-items:center;gap:5px}
.logo-mark{width:20px;height:20px;border-radius:50%;background:var(--green)}
.logo-name{font-family:"Jost",sans-serif;font-weight:600;font-size:17px;color:var(--navy)}
.logo-tag{left:160px;top:32px;font-size:4px;color:#999}
.call{left:281px;top:0;width:76px;height:42px;border-right:1px solid var(--line);display:flex;align-items:center}
.call-tab{width:14px;height:42px;background:var(--green);display:flex;align-items:flex-end;justify-content:center;padding-bottom:5px}
.call-text{padding-left:7px;font-size:6.5px;line-height:1.3;color:#444}
.contact{left:358px;top:0;width:106px;height:42px;border-right:1px solid var(--line);display:flex;align-items:center;gap:6px;padding-left:13px}
.contact b{display:block;font-weight:400;font-size:6px;color:#444}
.contact span{font-size:5px;color:#888}
.search{left:464px;top:0;width:46px;height:42px;display:flex;flex-direction:column;align-items:center;justify-content:center;gap:2px;font-size:5px;color:#666}
.menu{left:510px;top:0;width:43px;height:42px;background:var(--brand);color:#fff;display:flex;flex-direction:column;align-items:center;justify-content:center;gap:3px;font-size:5.5px;font-weight:700}

/* hero */
.hero{left:0;top:54px;width:688px;height:215px;background:linear-gradient(100deg,#e9c7bd 0%,#efe7e2 35%,#d7d6d4 55%,#3bb0c0 75%,#e3ecef 100%)}
.slogan{left:0;top:152px;width:688px;text-align:center;font-family:"Jost",sans-serif;font-size:13px;color:#fff;text-shadow:0 1px 3px rgba(0,0,0,.35)}

/* quick nav */
.quicknav{left:0;top:269px;width:688px;height:106px;background:var(--soft)}
.navbox{width:136px;height:20px;background:#fff;box-shadow:0 1px 2px rgba(0,0,0,.08);display:flex;align-items:center;justify-content:space-between;padding:0 1px 0 9px;font-family:"Jost",sans-serif;font-size:7.5px;color:#444}
.navbox i{width:9px;height:9px;border-radius:50%;background:var(--brand);display:flex;align-items:center;justify-content:center}

/* news */
.news-title{left:0;top:397px;width:688px}
.card{width:136px;height:39px;border:1px solid var(--line);background:#fff;display:flex;align-items:center;gap:6px;padding-left:6px}
.date{width:23px;height:23px;background:var(--brand);color:#fff;font-size:6.5px;line-height:1.15;text-align:center;display:flex;flex-direction:column;justify-content:center}
.card p{font-size:5.8px;line-height:1.45;color:#444}
.archive{left:480px;top:538px;width:73px;text-align:right;font-size:6px;font-weight:700;color:#7fa62b;text-decoration:underline}

/* careers */
.career-left{left:0;top:571px;width:134px;height:235px;background:linear-gradient(180deg,#dfe3ee 0%,#9aa5c8 100%)}
.career-right{left:410px;top:571px;width:278px;height:235px;background:linear-gradient(110deg,#b7d8df 0%,#6cbfba 40%,#d8e6a7 100%)}
.career{left:134px;top:571px;width:276px;height:235px;background:linear-gradient(180deg,#fff 0%,#f4f8fb 100%);text-align:center;padding:28px 24px 0}
.career .lead{font-size:7.2px;line-height:1.7;color:#333;margin-top:14px}
.career .body{font-size:5.3px;line-height:1.75;color:#555;margin-top:10px}
.btn{display:inline-block;margin-top:11px;width:61px;height:15px;line-height:15px;background:var(--brand);color:#fff;font-size:4.5px;font-weight:700}

/* social */
.social-title{left:0;top:830px;width:688px}
.profile{width:120px;text-align:center}
.photo{width:96px;height:96px;border-radius:50%;margin:0 auto;position:relative}
.badge{position:absolute;right:1px;top:9px;width:15px;height:15px;border-radius:50%;background:var(--blue);border:1.5px solid #fff}
.profile h3{font-family:"Jost",sans-serif;font-weight:500;font-size:8.5px;color:#333;margin-top:9px}
.profile a{font-size:5.5px;color:#555;display:block;margin-top:3px}

/* footer */
.footer{left:0;top:1034px;width:688px;height:166px;background:var(--soft)}
.f-logo{left:134px;top:1060px}
.f-about{left:134px;top:1096px;width:122px;font-size:5.3px;line-height:1.75;color:#555}
.f-col h4{font-size:5.3px;font-weight:700;color:#333;margin-bottom:8px;line-height:1.3}
.f-col li{list-style:none;font-size:4.8px;color:#555;margin-bottom:7px}
.f-col p{font-size:4.8px;color:#555;line-height:1.6;margin-bottom:5px}
.email{width:116px;height:20px;background:#fff;border:1px solid var(--line);display:flex;align-items:center;justify-content:space-between;padding:0 7px;font-size:5px;color:#666}
.f-social{display:flex;gap:5px;margin-top:10px}
.f-social i{width:13px;height:13px;border-radius:50%;background:#e4e4e4}
.copyright{left:0;top:1167px;width:688px;text-align:center;font-size:5px;color:#555}
</style>
</head>
<body>

<div class="abs topbar"><span>◷ MON. - FRI. 9:00 am - 6:00 pm</span><i class="dot"></i><i class="dot"></i><i class="dot"></i></div>

<header class="abs header">
  <div class="abs logo"><span class="logo-mark"></span><span class="logo-name">Kelmora</span></div>
  <div class="abs logo-tag">Omsorg Vård Boende</div>
  <div class="abs call">
    <div class="call-tab"><svg width="8" height="8" viewBox="0 0 10 10"><circle cx="5" cy="5" r="4.3" fill="none" stroke="#fff" stroke-width="0.9"/><path d="M3.4 3.2c.3 1.6 1.7 3 3.3 3.4l.6-.8-.9-.5-.5.4c-.6-.3-1.1-.8-1.4-1.4l.4-.5-.5-.9z" fill="#fff"/></svg></div>
    <div class="call-text">010-4417820<br><span style="font-size:5.5px;color:#777">info@kelmora.se</span></div>
  </div>
  <div class="abs contact">
    <svg width="15" height="12" viewBox="0 0 15 12"><rect x="1" y="1" width="9" height="6" rx="1" fill="none" stroke="var(--blue)"/><rect x="5" y="4" width="9" height="6" rx="1" fill="#fff" stroke="var(--blue)"/></svg>
    <div><b>KONTAKTA OSS</b><span>Fler kontaktuppgifter</span></div>
  </div>
  <div class="abs search"><svg width="11" height="11" viewBox="0 0 11 11"><circle cx="4.5" cy="4.5" r="3.5" fill="none" stroke="#333" stroke-width="1.3"/><path d="M7 7l3 3" stroke="#333" stroke-width="1.4"/></svg>SÖK</div>
  <div class="abs menu"><svg width="14" height="9" viewBox="0 0 14 9"><path d="M4 1h10M0 4.5h14M4 8h10" stroke="#fff" stroke-width="1.2"/></svg>MENY</div>
</header>

<div class="abs hero" role="img" aria-label="Foto: en sjuksköterska samtalar med en ung flicka"></div>
<p class="abs slogan">"Vi skapar Hållbara vägar till en Bättre framtid"</p>

<nav class="abs quicknav" aria-label="Snabblänkar"></nav>
<a class="abs navbox" style="left:134px;top:298px">HVB<i><svg width="4" height="5" viewBox="0 0 4 5"><path d="M1 .5l2 2-2 2" stroke="#fff" fill="none"/></svg></i></a>
<a class="abs navbox" style="left:275px;top:298px">Stödboende<i><svg width="4" height="5" viewBox="0 0 4 5"><path d="M1 .5l2 2-2 2" stroke="#fff" fill="none"/></svg></i></a>
<a class="abs navbox" style="left:415px;top:298px;width:138px">öppenvård<i><svg width="4" height="5" viewBox="0 0 4 5"><path d="M1 .5l2 2-2 2" stroke="#fff" fill="none"/></svg></i></a>
<a class="abs navbox" style="left:134px;top:327px">Vår Behandling<i><svg width="4" height="5" viewBox="0 0 4 5"><path d="M1 .5l2 2-2 2" stroke="#fff" fill="none"/></svg></i></a>
<a class="abs navbox" style="left:275px;top:327px">Om Kelmora<i><svg width="4" height="5" viewBox="0 0 4 5"><path d="M1 .5l2 2-2 2" stroke="#fff" fill="none"/></svg></i></a>
<a class="abs navbox" style="left:415px;top:327px;width:138px">Placering<i><svg width="4" height="5" viewBox="0 0 4 5"><path d="M1 .5l2 2-2 2" stroke="#fff" fill="none"/></svg></i></a>

<section>
  <div class="abs news-title"><h2>Nyheter</h2><div class="rule"></div></div>
  <article class="abs card" style="left:134px;top:436px"><div class="date">21<br>Dec</div><p>Lorem ipsum dolor sit amet,<br>consectetur adipiscing elit.</p></article>
  <article class="abs card" style="left:277px;top:436px"><div class="date">21<br>Dec</div><p>Lorem ipsum dolor sit amet,<br>consectetur adipiscing elit.</p></article>
  <article class="abs card" style="left:420px;top:436px;width:133px"><div class="date">21<br>Dec</div><p>Lorem ipsum dolor sit amet,<br>consectetur adipiscing elit.</p></article>
  <article class="abs card" style="left:134px;top:486px"><div class="date">21<br>Dec</div><p>Lorem ipsum dolor sit amet,<br>consectetur adipiscing elit.</p></article>
  <article class="abs card" style="left:277px;top:486px"><div class="date">21<br>Dec</div><p>Lorem ipsum dolor sit amet,<br>consectetur adipiscing elit.</p></article>
  <article class="abs card" style="left:420px;top:486px;width:133px"><div class="date">21<br>Dec</div><p>Lorem ipsum dolor sit amet,<br>consectetur adipiscing elit.</p></article>
  <a class="abs archive">Nyhetsarkivet ›</a>
</section>

<div class="abs career-left" role="img" aria-label="Foto: ung person i randig tröja"></div>
<section class="abs career">
  <h2>Jobba hos oss</h2>
  <p class="lead">Looking forward to becoming part of a business in progress with the vision of being the best? Then you may want to look at our company.</p>
  <p class="body">We are constantly looking to strengthen our team. Do you think that you can help develop the best care, care and accommodation, please feel free to contact you. We employ only persons with, according to the Social Board's own wording, people with adequate education. Which for us means at least 2 years of secondary education with a focus appropriate for the purpose. In our case, the focus may be abuse and social issues or the like.</p>
  <a class="btn">READ MORE</a>
</section>
<div class="abs career-right" role="img" aria-label="Foto: vårdpersonal vid ett fönster med gröna gardiner"></div>

<section>
  <div class="abs social-title"><h2>Kelmora i sociala medier</h2><div class="rule"></div></div>
  <div class="abs profile" style="left:146px;top:880px">
    <div class="photo" role="img" aria-label="Porträttfoto: leende kvinna" style="background:radial-gradient(circle at 50% 40%,#b89a84,#5d6670)"><i class="badge"></i></div>
    <h3>Lorem ipsum dolor</h3><a>Flöde ▸</a>
  </div>
  <div class="abs profile" style="left:283px;top:880px">
    <div class="photo" role="img" aria-label="Porträttfoto: kvinna som skriver vid ett bord" style="background:radial-gradient(circle at 50% 40%,#e2c99a,#a8bd6a)"><i class="badge"></i></div>
    <h3>Lorem ipsum dolor</h3><a>Videor ▸</a>
  </div>
  <div class="abs profile" style="left:421px;top:880px">
    <div class="photo" role="img" aria-label="Porträttfoto: ung kvinna i ett klassrum" style="background:radial-gradient(circle at 55% 45%,#d9bfa5,#8fa3b3)"><i class="badge"></i></div>
    <h3>Lorem ipsum dolor</h3><a>Nätverk ▸</a>
  </div>
</section>

<footer class="abs footer"></footer>
<div class="abs logo f-logo" style="top:1060px"><span class="logo-mark"></span><span class="logo-name">Kelmora</span></div>
<p class="abs f-about">Kelmora Sverige AB carries out care and care aimed at people aged 14-25 years. This is done primarily through Home for care and housing (HVB). We are specialists in psychosocial abuse and crime issues.</p>
<div class="abs f-col" style="left:277px;top:1071px">
  <h4>QUICK LINK</h4>
  <ul><li>Hem</li><li>Om Kelmora</li><li>Ängsgården HVB</li><li>Jobba hos oss</li><li>Kontakt</li></ul>
</div>
<div class="abs f-col" style="left:349px;top:1071px">
  <h4>GET IN TOUCH</h4>
  <p><b>Address:</b> Kelmora Sverige AB<br>Ekbacken 212<br>247 31 Sandvik</p>
  <p><b>Email:</b> info@kelmora.se</p>
  <p><b>Phone:</b> 010-4417820</p>
</div>
<div class="abs f-col" style="left:438px;top:1071px">
  <h4>SUBSCRIBE TO OUR E-MAIL LIST AND<br>STAY UP-TO DATE WITH ALL OUR NEWS.</h4>
  <div class="email">Email Address<svg width="8" height="7" viewBox="0 0 8 7"><path d="M0 3l8-3-2 7-2-3z" fill="var(--blue)"/></svg></div>
  <div class="f-social"><i></i><i></i><i></i></div>
</div>
<p class="abs copyright">Copyright © 2018 Kelmora. Personal Data · Availability · Cookies</p>

</body>
</html>
```